Bluebird Business Card Design

Name Marlene Obadofor
Title Mortgage Originator
Office (800) 416-2795 x65
Direct (240) 615-2079
Email mobadofor@bluebirdlending.example
NMLS 3817465
Licensed MD

Name Dorian Pelletier
Title Mortgage Originator
Office (800) 416-2795 x66
Direct (404) 263-5147
Email dpelletier@bluebirdlending.example
NMLS 3156702
Licensed MD

Name Rochelle Barnaby
Title Mortgage Originator
Office (800) 416-2795 x67
Direct (443) 812-3659
Email barnabyrochelle@mailpost.example
NMLS 3902576
Licensed MD

Name Omar Teldouri
Title Mortgage Originator
Office (800) 416-2795 x32
Direct (571) 326-7045
Email oteldouri@bluebirdlending.example
NMLS 1573064
Licensed MD

```html
<!DOCTYPE html>
<html lang="en">
<head>
<meta charset="utf-8">
<title>Bluebird Business Card Design</title>
<link rel="stylesheet" href="https://fonts.googleapis.com/css2?family=Lato:wght@400;700&display=swap">
<style>
  :root {
    --backdrop: #d3d4d6;
    --card: #ffffff;
    --ink: #111111;
    --ink-soft: #3a3a3a;
    --shadow: rgba(0, 0, 0, 0.18);
  }
  * { margin: 0; padding: 0; box-sizing: border-box; }
  html, body { width: 1200px; height: 877px; overflow: hidden; }
  body {
    background: var(--backdrop);
    font-family: "Lato", sans-serif;
    color: var(--ink);
    position: relative;
  }
  .card {
    position: absolute;
    width: 482px;
    height: 275px;
    background: var(--card);
    border-radius: 32px;
    box-shadow: 0 2px 6px var(--shadow);
    overflow: hidden;
  }
  .card--dorian  { left: 95px;  top: 118px; color: var(--ink-soft); }
  .card--marlene { left: 622px; top: 119px; }
  .card--rochelle{ left: 69px;  top: 479px; }
  .card--omar    { left: 621px; top: 486px; }

  .details {
    position: absolute;
    left: 48px;
    top: var(--text-top, 55px);
    width: 240px;
  }
  .name {
    font-weight: 700;
    font-size: 19.5px;
    line-height: 1;
    letter-spacing: -0.1px;
    white-space: nowrap;
  }
  .title {
    font-size: 13.2px;
    margin-top: 7px;
  }
  .contacts {
    list-style: none;
    margin-top: var(--list-gap, 14px);
  }
  .contacts li {
    display: flex;
    align-items: center;
    gap: 8px;
    font-size: 13.5px;
    height: 19.6px;
    white-space: nowrap;
  }
  .contacts svg { width: 15px; height: 13px; flex: none; fill: currentColor; }
  .license {
    font-size: 13.5px;
    line-height: 18px;
    margin-top: var(--license-gap, 6px);
  }
  .portrait {
    position: absolute;
    left: 300px;
    width: 156px;
    height: 156px;
    border-radius: 50%;
  }
  .card--dorian .portrait  { top: 62px; background: radial-gradient(circle at 50% 40%, #6b4632 0%, #3a2519 55%, #232a3e 100%); }
  .card--marlene .portrait { top: 60px; background: radial-gradient(circle at 50% 45%, #7a5238 0%, #3e2a1d 60%, #5d5a3e 100%); }
  .card--rochelle .portrait{ top: 62px; background: radial-gradient(circle at 50% 40%, #8a5a3c 0%, #6a4a2c 50%, #e8c9b2 100%); }
  .card--omar .portrait    { top: 65px; background: radial-gradient(circle at 50% 35%, #b08a72 0%, #4a3a30 45%, #a7a592 100%); }
</style>
</head>
<body>
<svg width="0" height="0" style="position:absolute">
  <defs>
    <symbol id="icon-office" viewBox="0 0 24 20"><path d="M2 7c0-3 5-5 10-5s10 2 10 5v2h-5V7c-1-1-3-1.5-5-1.5S8 6 7 7v2H2z"/><path d="M6 10h12l3 8H3z"/><rect x="9" y="12" width="6" height="4" fill="#fff"/></symbol>
    <symbol id="icon-direct" viewBox="0 0 24 24"><path d="M5 2l4 4-2 3c1 3 4 6 7 7l3-2 4 4-3 3C10 21 3 14 2 5z"/><path d="M14 3a7 7 0 0 1 7 7h-2a5 5 0 0 0-5-5zM14 7a3 3 0 0 1 3 3h-2a1 1 0 0 0-1-1z"/></symbol>
    <symbol id="icon-mail" viewBox="0 0 24 18"><path d="M1 1h22v16H1z"/><path d="M2 2l10 8 10-8" fill="none" stroke="#fff" stroke-width="2"/></symbol>
  </defs>
</svg>

<article class="card card--dorian">
  <div class="details">
    <h2 class="name">Dorian Pelletier</h2>
    <p class="title">Mortgage Originator</p>
    <ul class="contacts">
      <li><svg><use href="#icon-office"/></svg>(800) 416-2795 x66</li>
      <li><svg><use href="#icon-direct"/></svg>(404) 263-5147</li>
      <li><svg><use href="#icon-mail"/></svg>dpelletier@bluebirdlending.example</li>
    </ul>
    <p class="license">NMLS 3156702<br>Licensed MD</p>
  </div>
  <div class="portrait" role="img" aria-label="Portrait photo of Dorian Pelletier"></div>
</article>

<article class="card card--marlene" style="--text-top:58px; --list-gap:22px; --license-gap:14px;">
  <div class="details">
    <h2 class="name">Marlene Obadofor</h2>
    <p class="title">Mortgage Originator</p>
    <ul class="contacts">
      <li><svg><use href="#icon-office"/></svg>(800) 416-2795 x65</li>
      <li><svg><use href="#icon-direct"/></svg>(240) 615-2079</li>
      <li><svg><use href="#icon-mail"/></svg>mobadofor@bluebirdlending.example</li>
    </ul>
    <p class="license">NMLS 3817465<br>Licensed MD</p>
  </div>
  <div class="portrait" role="img" aria-label="Portrait photo of Marlene Obadofor"></div>
</article>

<article class="card card--rochelle" style="--text-top:58px; --list-gap:16px; --license-gap:14px;">
  <div class="details">
    <h2 class="name">Rochelle Barnaby</h2>
    <p class="title">Mortgage Originator</p>
    <ul class="contacts">
      <li><svg><use href="#icon-office"/></svg>(800) 416-2795 x67</li>
      <li><svg><use href="#icon-direct"/></svg>(443) 812-3659</li>
      <li><svg><use href="#icon-mail"/></svg>barnabyrochelle@mailpost.example</li>
    </ul>
    <p class="license">NMLS 3902576<br>Licensed MD</p>
  </div>
  <div class="portrait" role="img" aria-label="Portrait photo of Rochelle Barnaby"></div>
</article>

<article class="card card--omar" style="--text-top:59px; --list-gap:16px; --license-gap:12px;">
  <div class="details">
    <h2 class="name">Omar Teldouri</h2>
    <p class="title">Mortgage Originator</p>
    <ul class="contacts">
      <li><svg><use href="#icon-office"/></svg>(800) 416-2795 x32</li>
      <li><svg><use href="#icon-direct"/></svg>(571) 326-7045</li>
      <li><svg><use href="#icon-mail"/></svg>oteldouri@bluebirdlending.example</li>
    </ul>
    <p class="license">NMLS 1573064<br>Licensed MD</p>
  </div>
  <div class="portrait" role="img" aria-label="Portrait photo of Omar Teldouri"></div>
</article>
</body>
</html>
```